Internal Office Slogans / Motto / Vision Statements

Hi. We would like to put up some posters around the office with quotations such as -
-”Do what you do so well that they will want to see it again and bring their friends.”- Hollis Trevane
-Make your customers feel heard and understood. Make your customers feel respected and liked. Make your customers feel appreciated and helped. Understand that you can do none of these things unless you are sincere about them.
Gregory Pilcott
- It’s a very predictable and satisfying phenomenon: whenever we get better, our customers do too.
Ray Casso
-Catch people in the act of performing extraordinary customer service. Treat them like heroes. Tell their stories, far and wide.
Tod Brinkerley

The purpose of the posters is to reiterate our culture and vision within the organisation. They should be clean, crisp and eye catching, not gaudy or bright. Professional, bold and strong.

The company website and logo is at http://www.nexolux.com.au
Print size will be A1

Thanks for participating & looking forward to seeing your great work.
Updates

Hi All. . 

So to reiterate we are looking for one background design to be used for multiple quotes...  The list of quotes are as follows: 

Support and or Sales Office

 

Make your customers feel heard and understood.Make your customers feel respected and liked. Make your customers feelappreciated and helped. Understand that you can do none of these things unlessyou are sincere about them.

Gregory Pilcott

 

Nothing liberates our greatness like the desireto help, the desire to serve

Rosalind Penhallow

 

It’s a very predictable and satisfying phenomenon:whenever we get better, our customers do too.

Ray Casso

 

Success means we go to sleep at night knowingthat our talents and abilities were used in a way that served others.

Rosalind Penhallow.

 

The sole purpose of business is to create, serveand satisfy a customer, from beginning to end – and that’s everyone’s job.

Tod Brinkerley

 

We don’t celebrate closing a sale, we celebrateopening a relationship.

Gwendolyn Asque

I will never make you a promise – unless I giveyou a plan and procedure to make that promise possible.

Bo Tarrick

 

Customers feel we take them for granted; onlyshow interest when we want an order; lavish our time on prospects; communicatemainly by invoice; are fixated on big accounts; drop them like hot potatoesonce we have the order; don’t follow through on promises; and satisfy our ownbureaucracy rather than their needs. We can do better than that, much better.

Peter L Osmund.

 

 

General and public area

 

Catch people in the act of performingextraordinary customer service. Treat them like heroes. Tell their stories, farand wide.

Tod Brinkerley

 

 

We see our customers as invited guests to aparty, and we are the hosts. It’s our job every day to make every importantaspect of the customer experience a little bit better." Carl Ingvold - Founder andCEO of Veltrix

 

"If you do build a great experience,customers tell each other about that. Word of mouth is verypowerful."  Carl Ingvold

 

It's not a faithin technology. It's faith in people. Neil Corrby

 

“Being the richest man in the cemetery doesn’tmatter to me … Going to bed at night saying we’ve done something wonderful…that’s what matters to me.” Neil Corrby

 

The customer experience is the next competitivebattleground. Lance Merriwether, CIO, Quorra Computers

 

”Do what you do so well that they will want tosee it again and bring their friends.”- Hollis Trevane

In the world of internet customer service, it isimportant to remember your competitor is only a mouse click away. GlenTrasky (not sure who he is but like the quote).

The customer is why you go to work. If they goaway, you do, too. Martin Glossop (?)

 

MaybeSome for Sales or Build Team:

Quality is remembered long after the price is forgotten. Varenne Family Slogan

```html
<!DOCTYPE html>
<html lang="en">
<head>
<meta charset="utf-8">
<title>Customer Quote Poster</title>
<link rel="stylesheet" href="https://fonts.googleapis.com/css2?family=Saira+Condensed:wght@500&family=Pinyon+Script&display=swap">
<style>
  :root {
    --bg-centre: #3b3b3b;
    --bg-mid: #1c1c1c;
    --bg-edge: #070707;
    --quote-ink: #e7e4e4;
    --author-ink: #7083d8;
  }
  html, body {
    margin: 0;
    padding: 0;
    width: 848px;
    height: 1200px;
    overflow: hidden;
    background: var(--bg-edge);
  }
  .poster {
    position: relative;
    width: 848px;
    height: 1200px;
    overflow: hidden;
    background: radial-gradient(ellipse 70% 55% at 50% 50%, var(--bg-centre) 0%, var(--bg-mid) 55%, var(--bg-edge) 100%);
  }
  .quote {
    position: absolute;
    left: 86px;
    top: 96px;
    margin: 0;
    font-family: "Saira Condensed", "Arial Narrow", sans-serif;
    font-weight: 500;
    font-size: 58px;
    line-height: 84px;
    letter-spacing: 1.5px;
    text-transform: uppercase;
    color: var(--quote-ink);
  }
  .quote-line {
    display: block;
    white-space: nowrap;
  }
  .author {
    position: absolute;
    right: 34px;
    top: 1022px;
    margin: 0;
    font-family: "Pinyon Script", cursive;
    font-size: 40px;
    line-height: 1;
    color: var(--author-ink);
  }
</style>
</head>
<body>
  <main class="poster">
    <p class="quote">
      <span class="quote-line">Make your customers</span>
      <span class="quote-line">feel heard and understood.</span>
      <span class="quote-line">Make your customers feel</span>
      <span class="quote-line">respected and liked.</span>
      <span class="quote-line">Make your customers feel</span>
      <span class="quote-line">appreciated and helped.</span>
      <span class="quote-line">Understand that</span>
      <span class="quote-line">you can do none of these</span>
      <span class="quote-line">things unless you are</span>
      <span class="quote-line">sincere about them.</span>
    </p>
    <p class="author">Gregory Pilcott</p>
  </main>
</body>
</html>
```